Halvorn Hire Business Card Design

Need business cards designed for our new equipment rental. We specialize in renting to landscape / tree professionals, contractors, Do-It-Yourself'ers and Around the home or office. Looking for a eye catching card. Landscape and construction should be the theme. The logo is attached, and you can see our colors from the logo. You can use whatever color goes with it ok.

Target Market(s)

First off Landscape and Tree Professional. Then contractors, Do-It-Yourself'ers and rentals for Around the home or office.

Industry/Entity Type

Business

Contact Information for Business Card

Eye catching background that blends landscaping with construction equipment

Requirements
Must have
• Name on Card will Be: Derek Pollard (Manager)
• My Direct Phone Number is: 352-418-7093
• derek@halvornhire.example
• www.halvornhire.example
• 4172 Wexley Mill Road,
• Dade City FL 33590
Nice to have
• Would be Nice to have these bullets on the Face of the card that does not have all my information.
• Serving:
• Landscape / Tree Professionals
• Contractors
• DYI'ers or say Do-It-Yourself'ers
• Maybe have serving small and centered above these bullets, and these 3 bullets along the bottom of the card. Ideas?

```html
<!DOCTYPE html>
<html lang="en">
<head>
<meta charset="utf-8">
<title>Halvorn Hire Business Card</title>
<link rel="stylesheet" href="https://fonts.googleapis.com/css2?family=Montserrat:wght@800&family=Open+Sans:wght@400;600;700&display=swap">
<style>
  :root {
    --page-bg: #e6e4e1;
    --card-bg: #f3f1ee;
    --navy: #0f4470;
    --navy-text: #123f68;
    --steel: #9a9c9e;
    --ink: #2a2a2a;
    --white: #ffffff;
  }
  * { margin: 0; padding: 0; box-sizing: border-box; }
  html, body {
    width: 1200px; height: 900px; overflow: hidden;
    background: var(--page-bg);
    font-family: "Open Sans", Arial, sans-serif;
  }
  .card {
    position: absolute; left: 150px; top: 193px;
    width: 900px; height: 514px;
    background: var(--card-bg);
    box-shadow: 0 10px 30px rgba(0,0,0,.18);
    overflow: hidden;
  }
  .card-wedge { position: absolute; inset: 0; }
  .brand {
    position: absolute; left: 48px; top: 182px;
    display: flex; align-items: center; gap: 16px;
  }
  .brand-square { width: 30px; height: 30px; background: var(--navy); }
  .brand-name {
    font-family: "Montserrat", Arial, sans-serif; font-weight: 800;
    font-size: 54px; letter-spacing: 1px; color: var(--navy);
    text-transform: uppercase; line-height: 1;
  }
  .website {
    position: absolute; left: 156px; top: 284px;
    font-weight: 700; font-size: 17px; color: var(--navy-text);
  }
  .person { position: absolute; left: 46px; top: 400px; }
  .person-name {
    font-weight: 700; font-size: 26px; letter-spacing: .5px;
    color: var(--navy-text); text-transform: uppercase; line-height: 1.1;
  }
  .person-name .surname { color: var(--steel); }
  .person-title { font-size: 20px; color: var(--ink); margin-top: 2px; }
  .contact {
    position: absolute; right: 42px; top: 272px;
    color: var(--white); text-align: right; font-size: 20px; line-height: 30px;
    font-style: normal;
  }
  .contact-line { display: flex; justify-content: flex-end; align-items: center; gap: 8px; }
  .contact-line svg { width: 17px; height: 17px; fill: var(--white); }
  .address { margin-top: 18px; }
</style>
</head>
<body>
  <main class="card">
    <svg class="card-wedge" viewBox="0 0 900 514" aria-hidden="true">
      <path d="M900,10 L878,32 C862,62 840,90 790,98 L780,104 C700,170 420,390 318,468 C305,482 300,498 282,514 L900,514 Z" fill="var(--steel)"/>
      <path d="M900,30 L884,50 C870,80 850,104 808,112 L798,118 C720,182 440,400 344,474 C330,488 324,500 306,514 L900,514 Z" fill="var(--navy)"/>
    </svg>

    <div class="brand">
      <span class="brand-square"></span>
      <span class="brand-name">Halvorn Hire</span>
    </div>
    <p class="website">www.halvornhire.example</p>

    <div class="person">
      <p class="person-name">Derek <span class="surname">Pollard</span></p>
      <p class="person-title">Manager</p>
    </div>

    <address class="contact">
      <p class="contact-line">352-418-7093
        <svg viewBox="0 0 24 24"><path d="M3 9c0-3 4-5 9-5s9 2 9 5v2h-5V9H8v2H3zM6 12h12l2 8H4z"/></svg></p>
      <p class="contact-line">352-418-7094
        <svg viewBox="0 0 24 24"><path d="M7 2h10v20H7zM9 4v14h6V4z"/></svg></p>
      <p class="contact-line">352-418-7095
        <svg viewBox="0 0 24 24"><path d="M8 2h9v6H8zM4 9h16v13H4zM7 12v3h10v-3z"/></svg></p>
      <p class="contact-line">derek@halvornhire.example
        <svg viewBox="0 0 24 24"><path d="M2 5h20v14H2zM4 7v1l8 5 8-5V7l-8 5z"/></svg></p>
      <p class="address">4172 Wexley Mill Road,<br>Dade City FL 33590</p>
    </address>
  </main>
</body>
</html>
```